Harrowgate Oncology Centre

one page flyer -- I have two clinics inn two separate towns. I am trying to reach patients in these towns
I have attached the picture of my business card that caries my logo and other informations. In addition the Pine bluff clinic is associated with KBMC ( Caldwell Regional Memorial Hospital) and Little Rock clinc is associated with St Marlowe Hospital.
( these pictures were downloaded from zindex)
The caption is " your doctor, now at a place of your liking"

```html
<!DOCTYPE html>
<html lang="en">
<head>
<meta charset="utf-8">
<title>Harrowgate Oncology Centre – Flyer</title>
<link href="https://fonts.googleapis.com/css2?family=Source+Sans+3:wght@400;600&display=swap" rel="stylesheet">
<style>
  :root {
    --white: #ffffff;
    --ink: #1b1b1d;
    --navy: #2b3640;
    --magenta: #b03a86;
    --plum-light: #9a4f86;
    --plum-dark: #6b2d59;
    --panel-grey: #e5e5e6;
    --footer: #39393b;
    --footer-text: #f2f2f2;
    --office-pink: #ec8fae;
    --hero-light: #f4f5f6;
    --hero-mid: #dfe3e6;
  }
  * { box-sizing: border-box; margin: 0; padding: 0; }
  html, body { width: 926px; height: 1200px; overflow: hidden; background: var(--white); }
  body { font-family: "Source Sans 3", "Myriad Pro", sans-serif; color: var(--ink); }

  .flyer { position: relative; width: 926px; height: 1200px; }

  .header { position: relative; height: 200px; background: var(--white); }
  .brand { position: absolute; left: 34px; top: 42px; display: flex; align-items: center; gap: 18px; }
  .brand-square { width: 96px; height: 96px; background: var(--navy); }
  .brand-name { font-size: 34px; line-height: 1.05; font-weight: 400; color: var(--navy); width: 260px; }
  .site-url { position: absolute; right: 26px; top: 124px; font-size: 27px; color: var(--magenta); }

  .hero { position: relative; height: 487px; }
  .hero-photo { position: absolute; inset: 0;
    background: linear-gradient(90deg, var(--hero-light) 0%, var(--hero-light) 38%, var(--hero-mid) 70%, #cfd5da 100%); }
  .hero-headline { position: absolute; left: 33px; top: 122px; font-size: 45px; line-height: 53px;
    font-weight: 400; text-transform: uppercase; color: var(--ink); }

  .accent-band { height: 54px; background: linear-gradient(90deg, var(--plum-light), var(--plum-dark)); }

  .affiliates { position: relative; height: 322px; background: var(--panel-grey); }
  .affiliate { position: absolute; top: 41px; width: 387px; text-align: center; }
  .affiliate--little-rock { left: 58px; }
  .affiliate--pine-bluff { left: 480px; }
  .affiliate-photo { height: 193px; border: 2px solid #c9c9c9; }
  .affiliate-photo--st-marlowe { background: linear-gradient(180deg, #6f8fb8 0%, #a89aa6 40%, #b7764f 70%, #8a5638 100%); }
  .affiliate-photo--kbmc { background: linear-gradient(180deg, #4d8fd6 0%, #cfe0ef 35%, #f1f1ef 60%, #8a8c7a 100%); }
  .affiliate-caption { margin-top: 34px; font-size: 13px; line-height: 17px; font-weight: 600; color: var(--ink); }

  .offices { position: relative; height: 137px; background: var(--footer); color: var(--footer-text); }
  .office { position: absolute; top: 34px; }
  .office--little-rock { left: 58px; }
  .office--pine-bluff { left: 580px; }
  .office-title { font-size: 25px; font-weight: 400; color: var(--office-pink); margin-bottom: 8px; }
  .office-line { display: flex; align-items: center; gap: 10px; font-size: 14px; font-weight: 600; line-height: 24px; }
  .office-line svg { width: 12px; height: 12px; fill: var(--footer-text); flex: none; }
</style>
</head>
<body>
<main class="flyer">
  <header class="header">
    <div class="brand">
      <div class="brand-square"></div>
      <div class="brand-name">Harrowgate Oncology Centre</div>
    </div>
    <div class="site-url">www.harrowgateoncology.com</div>
  </header>

  <section class="hero">
    <div class="hero-photo" role="img" aria-label="Doctor in a white coat with stethoscope and red tie, arms crossed, in a bright clinic"></div>
    <h1 class="hero-headline">Your doctor,<br>now at a place<br>of your liking</h1>
  </section>

  <div class="accent-band"></div>

  <section class="affiliates">
    <figure class="affiliate affiliate--little-rock">
      <div class="affiliate-photo affiliate-photo--st-marlowe" role="img" aria-label="St Marlowe Hospital building exterior"></div>
      <figcaption class="affiliate-caption">Little Rock clinc is associated with<br>St Marlowe Hospital</figcaption>
    </figure>
    <figure class="affiliate affiliate--pine-bluff">
      <div class="affiliate-photo affiliate-photo--kbmc" role="img" aria-label="KBMC hospital entrance exterior"></div>
      <figcaption class="affiliate-caption">Pine bluff clinic is associated with KBMC<br>( Caldwell Regional Memorial Hospital</figcaption>
    </figure>
  </section>

  <footer class="offices">
    <div class="office office--little-rock">
      <h2 class="office-title">Little Rock Office</h2>
      <p class="office-line">
        <svg viewBox="0 0 24 24" aria-hidden="true"><path d="M6.6 10.8a15.1 15.1 0 0 0 6.6 6.6l2.2-2.2a1 1 0 0 1 1-.25 11.4 11.4 0 0 0 3.6.57 1 1 0 0 1 1 1V20a1 1 0 0 1-1 1A17 17 0 0 1 3 4a1 1 0 0 1 1-1h3.5a1 1 0 0 1 1 1c0 1.25.2 2.45.57 3.57a1 1 0 0 1-.25 1z"/></svg>
        501-555-0142 | 501-555-0187
      </p>
      <p class="office-line">
        <svg viewBox="0 0 24 24" aria-hidden="true"><path d="M12 2a7 7 0 0 0-7 7c0 5.25 7 13 7 13s7-7.75 7-13a7 7 0 0 0-7-7zm0 9.5A2.5 2.5 0 1 1 12 6.5a2.5 2.5 0 0 1 0 5z"/></svg>
        720 W. Larchmont Ave. Suite 210, 72205
      </p>
    </div>
    <div class="office office--pine-bluff">
      <h2 class="office-title">Pine Bluff Office</h2>
      <p class="office-line">
        <svg viewBox="0 0 24 24" aria-hidden="true"><path d="M6.6 10.8a15.1 15.1 0 0 0 6.6 6.6l2.2-2.2a1 1 0 0 1 1-.25 11.4 11.4 0 0 0 3.6.57 1 1 0 0 1 1 1V20a1 1 0 0 1-1 1A17 17 0 0 1 3 4a1 1 0 0 1 1-1h3.5a1 1 0 0 1 1 1c0 1.25.2 2.45.57 3.57a1 1 0 0 1-.25 1z"/></svg>
        870-555-0163 | 870-555-0119
      </p>
      <p class="office-line">
        <svg viewBox="0 0 24 24" aria-hidden="true"><path d="M12 2a7 7 0 0 0-7 7c0 5.25 7 13 7 13s7-7.75 7-13a7 7 0 0 0-7-7zm0 9.5A2.5 2.5 0 1 1 12 6.5a2.5 2.5 0 0 1 0 5z"/></svg>
        1825 S. Willowbank St. Pine Bluff 71603
      </p>
    </div>
  </footer>
</main>
</body>
</html>
```